Mosquito and outdoor pest management

The uploaded logo must be integrated as the main theme of the card. I would like it to be modern and eye catching. Maybe some backround images or light silver metallic background.
Space enough at the base for contact info to be put in- phone numbers,emails,names,website.
Space on the back for short blog and lines for hand writing..calling card.
Commercial- golf courses, schools, outdoor function properties, pre event treatments.
Residential- retirement villages, townhome complexes and general houses
Management

```html
<!DOCTYPE html>
<html lang="en">
<head>
<meta charset="utf-8">
<title>Bayline Outdoor Care – Business Card</title>
<link href="https://fonts.googleapis.com/css2?family=Noto+Serif:wght@500&family=Arimo&family=Open+Sans&display=swap" rel="stylesheet">
<style>
  :root {
    --stage: #2a2a2a;
    --card: #f0f0f0;
    --brand-red: #e0262e;
    --ink: #1a1a1a;
    --rule: #5a5a5a;
    --white: #ffffff;
  }
  * { margin: 0; padding: 0; box-sizing: border-box; }
  html, body { width: 1200px; height: 800px; overflow: hidden; background: var(--stage); }
  .stage { position: relative; width: 1200px; height: 800px; }
  .card {
    position: absolute; top: 238px; width: 536px; height: 306px;
    background: var(--card); overflow: hidden;
  }
  .card--front { left: 49px; }
  .card--back { left: 617px; }
  .card__wave { position: absolute; inset: 0; }

  .brand {
    position: absolute; display: flex; align-items: center; gap: 12px;
    font-family: "Noto Serif", serif; font-weight: 500; font-size: 32px; line-height: 1;
    color: var(--ink); white-space: nowrap;
  }
  .brand__mark { width: 16px; height: 16px; border-radius: 50%; background: var(--brand-red); flex: none; }
  .card--front .brand { left: 84px; top: 72px; }
  .card--back .brand { left: 30px; top: 56px; }

  .holder {
    position: absolute; left: 63px; top: 204px;
    font-family: "Noto Serif", serif; font-weight: 500; font-size: 25px; color: var(--white);
  }
  .contact-divider { position: absolute; left: 269px; top: 218px; width: 2px; height: 60px; background: var(--white); }
  .contact { position: absolute; left: 292px; top: 220px; list-style: none;
    font-family: "Open Sans", sans-serif; font-size: 14px; color: var(--white); }
  .contact li { display: flex; align-items: center; gap: 12px; height: 20.5px; }
  .contact svg { width: 11px; height: 11px; flex: none; }

  .back-rule { position: absolute; left: 0; right: 0; top: 125px; height: 2px; background: var(--rule); }
  .service { position: absolute; top: 144px; }
  .service--commercial { left: 25px; }
  .service--residential { left: 310px; }
  .service__title { font-family: "Noto Serif", serif; font-weight: 500; font-size: 28px; color: var(--brand-red); line-height: 1; margin-bottom: 14px; }
  .service__list { list-style: none; font-family: "Arimo", sans-serif; font-size: 17px; color: var(--ink); }
  .service__list li { display: flex; align-items: center; height: 23.5px; white-space: nowrap; }
  .service__list li::before { content: "\2731"; color: var(--brand-red); font-size: 13px; width: 24px; padding-left: 2px; }
</style>
</head>
<body>
<main class="stage">

  <section class="card card--front" aria-label="Card front">
    <svg class="card__wave" viewBox="0 0 536 306" aria-hidden="true">
      <path d="M0 152 Q268 204 536 154 L536 306 L0 306 Z" fill="var(--brand-red)"/>
      <path d="M0 131 Q268 188 536 132" fill="none" stroke="var(--ink)" stroke-width="6"/>
    </svg>
    <div class="brand"><span>Bayline Outdoor Care</span><span class="brand__mark"></span></div>
    <p class="holder">Owen Hartley</p>
    <div class="contact-divider"></div>
    <ul class="contact">
      <li><svg viewBox="0 0 11 11"><rect width="11" height="11" rx="1.5" fill="#fff"/><path d="M3 3.5h5v1.2H3zM4 6h3v2.5H4z" fill="var(--brand-red)"/></svg>+1 555 014 2290</li>
      <li><svg viewBox="0 0 11 11"><rect width="11" height="11" rx="1.5" fill="#fff"/><path d="M2.5 3.5h6v4h-6z M2.5 3.5l3 2.2 3-2.2" fill="none" stroke="var(--brand-red)" stroke-width="0.9"/></svg>hello@bayline.com</li>
      <li><svg viewBox="0 0 11 11"><rect width="11" height="11" rx="1.5" fill="#fff"/><circle cx="5.5" cy="5.5" r="3" fill="none" stroke="var(--brand-red)" stroke-width="1"/></svg>www.baylinecare.com</li>
    </ul>
  </section>

  <section class="card card--back" aria-label="Card back">
    <div class="brand"><span>Bayline Outdoor Care</span><span class="brand__mark"></span></div>
    <div class="back-rule"></div>
    <div class="service service--commercial">
      <h2 class="service__title">Commercial</h2>
      <ul class="service__list">
        <li>golf courses</li>
        <li>schools</li>
        <li>outdoor function properties</li>
        <li>pre event treatments</li>
      </ul>
    </div>
    <div class="service service--residential">
      <h2 class="service__title">Residential</h2>
      <ul class="service__list">
        <li>retirement villages</li>
        <li>townhome complexes</li>
        <li>general houses</li>
      </ul>
    </div>
  </section>

</main>
</body>
</html>
```